Letterhead Design Project

Looking for letterhead designs for Dravesco Mining.

I am looking for a letterhead design in conjunction with a business card design. I have opened contests for both but ask that if you submit a letterhead design you also submit a business card design with a corresponding look/feel.

Dravesco Mining is a B2B company that buys and sells large machinery tires within the coal mining industry. The design should the strong, crisp and masculine. I have uploaded the company logo and mock-up of the back of the company's business card.

Color scheme should be grey/green/black

Contact information to include:
Name: Tom Sealbrook
Title: Managing Director
Phone: 555-314-2097
Address: 1186 Pelham #3 Dallas, TX 75209
Email: Tom@Dravesco.example

Project Deadline Extended
Reason: Looking for a more refined, elegant letterhead than what's been submitted as of yet. Here is a sample of what we're looking for: http://www.plumbridgestudio.example/letterhead-designs/ We will also be increasing the payment.

```html
<!DOCTYPE html>
<html lang="en">
<head>
<meta charset="utf-8">
<title>Dravesco Mining Letterhead</title>
<link href="https://fonts.googleapis.com/css2?family=Roboto:wght@400;500&display=swap" rel="stylesheet">
<style>
  :root {
    --backdrop: #e4e5e6;
    --paper: #ffffff;
    --band-dark: #15171a;
    --band-mid: #2c2f33;
    --band-light: #44484d;
    --brand-green: #6cb33f;
    --brand-white: #f2f3f4;
    --ink-grey: #555a5f;
  }
  * { margin: 0; padding: 0; box-sizing: border-box; }
  html, body {
    width: 1138px;
    height: 1200px;
    overflow: hidden;
    background: var(--backdrop);
  }
  .letterhead {
    position: absolute;
    left: 159px;
    top: 20px;
    width: 820px;
    height: 1160px;
    background: var(--paper);
    box-shadow: 0 2px 10px rgba(0, 0, 0, 0.12);
  }
  .header-band {
    position: absolute;
    left: 0;
    top: 0;
    width: 100%;
    height: 130px;
  }
  .header-texture {
    position: absolute;
    inset: 0;
    background: linear-gradient(180deg, var(--band-light) 0%, var(--band-mid) 30%, var(--band-dark) 60%, var(--band-mid) 100%);
  }
  .brand {
    position: absolute;
    left: 0;
    right: 0;
    top: 46px;
    display: flex;
    justify-content: center;
    align-items: center;
    gap: 14px;
  }
  .brand-square {
    width: 30px;
    height: 30px;
    background: var(--brand-green);
  }
  .brand-name {
    font-family: "Roboto", Arial, sans-serif;
    font-weight: 500;
    font-size: 38px;
    letter-spacing: 1px;
    text-transform: uppercase;
    color: var(--brand-white);
  }
  .contact-footer {
    position: absolute;
    left: 0;
    right: 0;
    bottom: 42px;
    text-align: center;
    font-family: "Roboto", Arial, sans-serif;
    font-size: 16px;
    color: var(--ink-grey);
    line-height: 28px;
  }
  .contact-line span + span { margin-left: 22px; }
  .contact-label {
    color: var(--brand-green);
    font-weight: 500;
  }
</style>
</head>
<body>
  <main class="letterhead">
    <header class="header-band">
      <div class="header-texture" role="img" aria-label="Dark perforated metal texture"></div>
      <div class="brand">
        <div class="brand-square"></div>
        <div class="brand-name">Dravesco Mining</div>
      </div>
    </header>
    <footer class="contact-footer">
      <p class="contact-address">1186 Pelham #3 Dallas, TX 75209</p>
      <p class="contact-line">
        <span><span class="contact-label">Ph:</span> 555-314-2097</span><span><span class="contact-label">E:</span> Tom@Dravesco.example</span>
      </p>
    </footer>
  </main>
</body>
</html>
```